Ironleaf Personal Training Studio Information Card

The front and back of card to give people that walk in to our gym. There are a few things to say on the card. But it also needs to be designed in an attractive way. You can make some of the information bullett points or with icons or graphics. Please look at our website at https://ironleaftraining.com/ . The card will be 4" x 9"

Target Market(s)

High End Clientele who want to train in a private gym

Industry/Entity Type

Fitness

Font styles to use
Serif
Sans Serif
Other font styles liked:
• the same font Velto uses on the zelpad

Colors
F0912C
F2A743
F7CA91
FBE8D2
FDF5EE

Requirements
Must have
• A cool look

```html
<!DOCTYPE html>
<html lang="en">
<head>
<meta charset="utf-8">
<title>Ironleaf Personal Training Studio – Information Card</title>
<link href="https://fonts.googleapis.com/css2?family=Roboto+Condensed:ital,wght@0,400;0,700;1,400;1,700;1,800&family=Roboto:wght@400;500;700&display=swap" rel="stylesheet">
<style>
  :root{
    --page:#e4e4e4;
    --card:#15171b;
    --card-deep:#0c0d10;
    --accent:#ec5126;
    --accent-soft:rgba(236,81,38,.55);
    --ink:#ffffff;
    --ink-soft:#e9e9e9;
  }
  *{margin:0;padding:0;box-sizing:border-box}
  html,body{width:1200px;height:1200px;overflow:hidden;background:var(--page)}
  .canvas{position:relative;width:1200px;height:1200px}
  .card{position:absolute;top:106px;width:454px;height:987px;overflow:hidden;
    background:linear-gradient(180deg,var(--card) 0%,var(--card-deep) 100%);
    color:var(--ink);font-family:"Roboto Condensed",sans-serif;
    box-shadow:0 10px 30px rgba(0,0,0,.35)}
  .card--front{left:109px}
  .card--back{left:632px}
  .photo{position:absolute}
  .photo--trainer{left:0;top:0;width:454px;height:640px;
    background:linear-gradient(180deg,#3a3f46 0%,#4d4a48 35%,#3b2f2a 60%,rgba(21,23,27,0) 100%)}
  .photo--athlete{left:250px;top:0;width:204px;height:720px;
    background:radial-gradient(ellipse at 60% 40%,#b9562e 0%,#6b2d19 40%,rgba(21,23,27,0) 75%)}
  .stripes{position:absolute;inset:0;width:454px;height:987px}
  .abs{position:absolute}
  .brand{right:40px;top:55px;font-family:"Roboto",sans-serif;font-weight:700;font-size:38px;letter-spacing:1px;display:flex;align-items:center;gap:8px}
  .brand-mark{width:12px;height:12px;background:var(--accent)}
  .headline-test{left:36px;top:330px;font-style:italic;font-weight:700;font-size:58px;letter-spacing:6px;color:var(--accent)}
  .headline-flex{left:32px;top:378px;font-style:italic;font-weight:700;font-size:122px;letter-spacing:22px;color:var(--ink);line-height:1}
  .body{font-family:"Roboto Condensed",sans-serif;font-size:16px;line-height:19.4px;letter-spacing:1px;color:var(--ink-soft)}
  .front-body{left:33px;top:527px;width:300px}
  .section-title{font-style:italic;font-weight:700;color:var(--accent);letter-spacing:4px;font-size:33px}
  .front-title{left:116px;top:732px}
  .services{list-style:none}
  .service{position:absolute;display:flex;align-items:center;gap:6px;font-size:14px;letter-spacing:1px}
  .service svg{width:24px;height:24px}
  .back-head{left:42px;top:30px;font-style:italic;font-weight:700;line-height:1}
  .back-head .big{display:block;font-size:62px;color:var(--accent);letter-spacing:2px;margin-left:4px}
  .back-head .small{display:block;font-size:31px;color:var(--ink);letter-spacing:1px;margin:6px 0 14px}
  .back-body{left:33px;top:271px;width:400px}
  .back-body p+p{margin-top:19px}
  .rates-title{left:130px;top:522px}
  .rates-note{left:35px;top:575px;font-weight:700;font-size:16px;letter-spacing:1px}
  .rates{left:47px;top:611px;list-style:none}
  .rate{display:flex;align-items:center;gap:12px;height:35.6px;font-size:16px;letter-spacing:1px}
  .rate svg{width:14px;height:10px}
  .rule{height:2px;background:var(--accent-soft)}
  .rule--one{left:210px;top:750px;width:210px}
  .rule--two{left:36px;top:876px;width:200px}
  .example-label{left:40px;top:760px;font-weight:700;font-size:16px;letter-spacing:1px;color:var(--accent)}
  .example{left:40px;top:796px;font-style:italic;font-size:16px;line-height:18px;letter-spacing:1px}
  .contact{font-family:"Roboto",sans-serif;font-size:13px;letter-spacing:1px;display:flex;align-items:center;gap:8px}
  .contact .dot{width:16px;height:16px;border-radius:50%;background:var(--accent);display:inline-flex;align-items:center;justify-content:center}
  .contact .dot svg{width:10px;height:10px}
</style>
</head>
<body>
<div class="canvas">

  <!-- FRONT -->
  <section class="card card--front">
    <div class="photo photo--trainer" role="img" aria-label="Photo of a female trainer coaching a man doing dumbbell curls in a gym"></div>
    <svg class="stripes" viewBox="0 0 454 987" aria-hidden="true">
      <polygon points="380,0 454,0 454,80" fill="#ec5126" opacity=".85"/>
      <polygon points="330,100 454,100 454,220" fill="#ec5126" opacity=".4"/>
      <polygon points="28,405 130,405 454,730 454,830" fill="#ec5126" opacity=".45"/>
      <polygon points="180,470 260,470 454,665 454,745" fill="#ec5126" opacity=".35"/>
      <polygon points="15,788 140,788 240,888 115,888" fill="#ec5126" opacity=".85"/>
      <polygon points="320,830 380,830 454,904 454,964" fill="#ec5126" opacity=".5"/>
      <polygon points="0,915 0,987 72,987" fill="#ec5126" opacity=".9"/>
    </svg>
    <div class="abs brand"><span class="brand-mark"></span>IRONLEAF</div>
    <div class="abs headline-test">TEST YOUR</div>
    <div class="abs headline-flex">FLEX</div>
    <p class="abs body front-body">We schedule prospective clients for a no cost or obligation consultation. At that consultation we will do a movement screen with you. This will allow the trainer to see what level of flexibility and strength you are currently at. You will be able to discuss your goals and other issues (injuries, etc) at that time.</p>
    <h2 class="abs section-title front-title">WHAT WE DO</h2>
    <ul class="services">
      <li class="service" style="left:70px;top:809px"><svg viewBox="0 0 24 24"><circle cx="12" cy="13" r="10" fill="#fff"/><circle cx="12" cy="11" r="4" fill="#15171b"/></svg>Weight Loss</li>
      <li class="service" style="left:252px;top:809px"><svg viewBox="0 0 24 24" fill="#fff"><rect x="1" y="7" width="3" height="10"/><rect x="5" y="4" width="3" height="16"/><rect x="8" y="11" width="8" height="2"/><rect x="16" y="4" width="3" height="16"/><rect x="20" y="7" width="3" height="10"/></svg>Build Strength</li>
      <li class="service" style="left:70px;top:852px"><svg viewBox="0 0 24 24" fill="#fff"><circle cx="12" cy="12" r="10"/></svg>Increase Flexibility</li>
      <li class="service" style="left:252px;top:852px"><svg viewBox="0 0 24 24" fill="none" stroke="#fff" stroke-width="2"><rect x="2" y="6" width="20" height="12" rx="2"/><path d="M6 18v-4M10 18v-3M14 18v-4M18 18v-3"/></svg>Body Sculpting</li>
      <li class="service" style="left:70px;top:896px"><svg viewBox="0 0 24 24" fill="#fff"><rect x="2" y="16" width="20" height="5" rx="2"/><circle cx="12" cy="7" r="4"/></svg>Functional Movement</li>
      <li class="service" style="left:252px;top:896px"><svg viewBox="0 0 24 24" fill="none" stroke="#fff" stroke-width="2"><circle cx="10" cy="13" r="7"/><path d="M17 6l4-4"/></svg>Improve Health</li>
    </ul>
  </section>

  <!-- BACK -->
  <section class="card card--back">
    <div class="photo photo--athlete" role="img" aria-label="Photo of a muscular arm lifting a dumbbell"></div>
    <svg class="stripes" viewBox="0 0 454 987" aria-hidden="true">
      <polygon points="380,0 454,0 454,74" fill="#ec5126" opacity=".85"/>
      <polygon points="335,62 395,62 454,121 454,181" fill="#ec5126" opacity=".5"/>
      <polygon points="260,280 300,280 454,434 454,474" fill="#ec5126" opacity=".35"/>
      <polygon points="20,367 85,367 290,572 225,572" fill="#ec5126" opacity=".45"/>
      <polygon points="150,580 200,580 380,760 330,760" fill="#ec5126" opacity=".3"/>
      <polygon points="200,848 260,848 400,987 340,987" fill="#ec5126" opacity=".8"/>
      <polygon points="0,910 0,987 77,987" fill="#ec5126" opacity=".9"/>
    </svg>
    <h1 class="abs back-head">
      <span class="big">SAFE</span>
      <span class="small">AND INDIVIDUALIZED</span>
      <span class="big">APPROACH</span>
      <span class="small">TO STRENGTH TRAINING</span>
    </h1>
    <div class="abs body back-body">
      <p>Our clients have different goals: Build strength, Increase Flexibility, Improve functional and daily movements, Train for an event, or Weight Loss. We will tailor your training program to the specific results you are looking for.</p>
      <p>Some ways of training increase the chance of injury, we do not practice those types of training at Ironleaf. Many of our clients have current or past injuries that can cause problems. We work with them to not aggravate those injuries or allow them to become an obstacle to their workouts.</p>
    </div>
    <h2 class="abs section-title rates-title">OUR RATES</h2>
    <p class="abs rates-note">All Sessions are 60 minutes</p>
    <ul class="abs rates">
      <li class="rate"><svg viewBox="0 0 14 10" fill="#ec5126"><rect x="0" y="2" width="2" height="6"/><rect x="3" y="0" width="2" height="10"/><rect x="5" y="4" width="4" height="2"/><rect x="9" y="0" width="2" height="10"/><rect x="12" y="2" width="2" height="6"/></svg>1 time per week:&nbsp; $110 per session</li>
      <li class="rate"><svg viewBox="0 0 14 10" fill="#ec5126"><rect x="0" y="2" width="2" height="6"/><rect x="3" y="0" width="2" height="10"/><rect x="5" y="4" width="4" height="2"/><rect x="9" y="0" width="2" height="10"/><rect x="12" y="2" width="2" height="6"/></svg>2 times per week: $85 per session</li>
      <li class="rate"><svg viewBox="0 0 14 10" fill="#ec5126"><rect x="0" y="2" width="2" height="6"/><rect x="3" y="0" width="2" height="10"/><rect x="5" y="4" width="4" height="2"/><rect x="9" y="0" width="2" height="10"/><rect x="12" y="2" width="2" height="6"/></svg>3 times per week $80 per session</li>
      <li class="rate"><svg viewBox="0 0 14 10" fill="#ec5126"><rect x="0" y="2" width="2" height="6"/><rect x="3" y="0" width="2" height="10"/><rect x="5" y="4" width="4" height="2"/><rect x="9" y="0" width="2" height="10"/><rect x="12" y="2" width="2" height="6"/></svg>Add $40 for a Partnered Session</li>
    </ul>
    <div class="abs rule rule--one"></div>
    <p class="abs example-label">Example:</p>
    <p class="abs example">A Partnered Session<br>(2 people training together) coming twice a week is<br>$125 per session</p>
    <div class="abs rule rule--two"></div>
    <div class="abs contact" style="left:40px;top:904px"><span class="dot"><svg viewBox="0 0 10 10" fill="#fff"><path d="M2 1l2 2-1 1c.5 1.2 1.5 2.2 2.7 2.7l1-1 2 2-1.2 1.3C4 9 1 6 .8 2.2z"/></svg></span>(555) 014-2277</div>
    <div class="abs contact" style="left:40px;top:929px"><span class="dot"></span>ironleafgym</div>
    <div class="abs contact" style="left:185px;top:904px"><span class="dot"><svg viewBox="0 0 10 10" fill="none" stroke="#fff" stroke-width="1.2"><rect x="1" y="2" width="8" height="6"/><path d="M1 2l4 3 4-3"/></svg></span>contact@ironleaftraining.com</div>
    <div class="abs contact" style="left:185px;top:929px"><span class="dot"><svg viewBox="0 0 10 10" fill="none" stroke="#fff" stroke-width="1"><circle cx="5" cy="5" r="4"/><path d="M1 5h8M5 1c-2 2.5-2 5.5 0 8M5 1c2 2.5 2 5.5 0 8"/></svg></span>www.ironleaftraining.com</div>
  </section>

</div>
</body>
</html>
```